Audio Plinth business card

Need a new business card design. Something that would ideally mesh the world of audio with the world of technology. I am posting some graphics as ideas, as well as my current business card and logo, which could use refreshing as well.
Looking for something hi-tech, but clean

Target Market(s)

hi tech audio people

Contact Information for Business Card

Corbin Maltby
President
248 Orchard Row
Harlow Springs, NV
91735
corbin@audioplinth.example
Office 555. 214. 3087
Mobile 555. 762. 4391

Font styles to use
Sans Serif

Colors

Designer to choose colors to be used in the design.

Requirements
Must have
• Some reference to audio and technology
Nice to have
• 3D look to logo or audio wave (or something else if you have ideas!)
Should not have
• Pretty open to other creative ideas

```html
<!DOCTYPE html>
<html lang="en">
<head>
<meta charset="utf-8">
<title>Audio Plinth – Business Card</title>
<link rel="stylesheet" href="https://fonts.googleapis.com/css2?family=Lato:wght@400;700;900&display=swap">
<style>
  :root {
    --stage: #e2904e;
    --card: #1b1b1c;
    --card-edge: #141415;
    --silver-light: #d9dde2;
    --silver: #a9afb6;
    --accent-line: #5f7d95;
    --contact-text: #a7a9ac;
    --icon: #9a9da1;
  }
  * { box-sizing: border-box; margin: 0; padding: 0; }
  html, body {
    width: 1200px;
    height: 755px;
    overflow: hidden;
    background: var(--stage);
    font-family: "Lato", "Helvetica Neue", Arial, sans-serif;
  }
  .stage {
    width: 1200px;
    height: 755px;
    display: flex;
    align-items: center;
    justify-content: center;
  }
  .business-card {
    position: relative;
    width: 1050px;
    height: 600px;
    background: radial-gradient(ellipse at 45% 35%, #232324 0%, var(--card) 55%, var(--card-edge) 100%);
    box-shadow: 0 18px 40px rgba(0, 0, 0, 0.35);
  }
  .holder {
    position: absolute;
    left: 62px;
    top: 100px;
  }
  .holder-name {
    font-weight: 700;
    font-size: 54px;
    letter-spacing: 1px;
    line-height: 1;
    color: var(--silver);
    background: linear-gradient(180deg, var(--silver-light) 0%, var(--silver) 55%, #7e858c 100%);
    -webkit-background-clip: text;
    background-clip: text;
    -webkit-text-fill-color: transparent;
  }
  .holder-title {
    display: inline-block;
    margin-top: 16px;
    padding-bottom: 5px;
    font-weight: 700;
    font-size: 19px;
    letter-spacing: 2.5px;
    color: var(--silver);
    border-bottom: 3px solid var(--accent-line);
  }
  .contact-list {
    position: absolute;
    left: 62px;
    bottom: 44px;
    list-style: none;
  }
  .contact-item {
    display: flex;
    align-items: center;
    height: 43px;
    font-size: 23px;
    color: var(--contact-text);
    white-space: nowrap;
  }
  .contact-icon {
    width: 26px;
    height: 26px;
    margin-right: 20px;
    fill: var(--icon);
    flex-shrink: 0;
  }
  .brand {
    position: absolute;
    right: 60px;
    bottom: 96px;
    display: flex;
    align-items: center;
    gap: 12px;
  }
  .brand-mark {
    width: 16px;
    height: 16px;
    background: var(--silver);
  }
  .brand-name {
    font-weight: 900;
    font-size: 34px;
    letter-spacing: 1px;
    text-transform: uppercase;
    color: var(--silver);
  }
</style>
</head>
<body>
<main class="stage">
  <section class="business-card" aria-label="Audio Plinth business card">
    <header class="holder">
      <h1 class="holder-name">CORBIN MALTBY</h1>
      <p class="holder-title">PRESIDENT</p>
    </header>

    <ul class="contact-list">
      <li class="contact-item">
        <svg class="contact-icon" viewBox="0 0 24 24" aria-hidden="true"><path d="M2 6h20v12H2z M3.5 7.2 12 13l8.5-5.8" fill="none" stroke="#9a9da1" stroke-width="1.6"/><path d="M2 6h20L12 12.8z"/></svg>
        corbin@audioplinth.example
      </li>
      <li class="contact-item">
        <svg class="contact-icon" viewBox="0 0 24 24" aria-hidden="true"><path d="M3 9c0-3 4-5 9-5s9 2 9 5v2h-5V9H8v2H3z"/><path d="M6 12h12l2 8H4z"/><circle cx="12" cy="16" r="2" fill="#1b1b1c"/></svg>
        555. 214. 3087 (Office)
      </li>
      <li class="contact-item">
        <svg class="contact-icon" viewBox="0 0 24 24" aria-hidden="true"><path d="M7 2h10a1.5 1.5 0 0 1 1.5 1.5v17A1.5 1.5 0 0 1 17 22H7a1.5 1.5 0 0 1-1.5-1.5v-17A1.5 1.5 0 0 1 7 2zm0.5 3v13h9V5z"/><circle cx="12" cy="20" r="0.9" fill="#1b1b1c"/></svg>
        555. 762. 4391 (Mobile)
      </li>
      <li class="contact-item">
        <svg class="contact-icon" viewBox="0 0 24 24" aria-hidden="true"><path d="M12 3 2 12h3v9h5v-6h4v6h5v-9h3z"/></svg>
        248 Orchard Row, Harlow Springs, NV 91735
      </li>
    </ul>

    <div class="brand">
      <span class="brand-mark" aria-hidden="true"></span>
      <span class="brand-name">Audio Plinth</span>
    </div>
  </section>
</main>
</body>
</html>
```